Ripplesound 90's Revival club night

I am after either an A5 or DL flyer but also the formats for using the design on social media etc.
The flyer is for a 90's revival club night at a nightclub that was well attended in the 90's . A special guest PA - Lulu K famous for her single 'Hold on to the starlight' ,is performing.
I have a logo for the night that may have to be altered / edited to fit in with your design (Colours changed etc) but also have a logo for the artist that may be more restrictive in regards to any changes.Both are attached.
Look forward to hearing from you shortly,

Tam

Reason: Required text to go on the flyer has now be added to the brief. Majority of designs submitted didn't seem to reflect to '90's nightclub' feel we were hoping for. Most of the designs used the colour scheme based on the 'Ripplesound' logo. We are hoping that these colours can be ignored with some designs and that the logo is made of of different colours that would make it easier for it to fit in with the designers ideas. Regards Tam

Target Market(s)

20 to 50 years age range who use to go clubbing / still do / love the 90's music. Club that they use to attend in the 90's is where the event is being held

Industry/Entity Type

Club

Requirements
Must have
• Both the logos for the event ( Ripplesound 90's Revival and Lulu K ) must be included on the flyer. Colours and the format can be altered on the ripplesound logo but the design should remain as close to the original as sent. 90's font and images would also be a must if possible. Lulu K logo can have colors altered, but not the font or design.
• Text required as follows :
• Venue : Club Vortex, Fenwick Lane, Westbury, Wiltshire
• Date : Saturday 10th June 2017
• Time : 8.30pm till 3am
• Very special guest PA ‘ LULU K’ ‘Hold on to the starlight’
• DJ’s : Main room – Dezzy Palmer ( North 38 / Ripplesound )
• Room 2 – Marcus J
• Full club décor with Laser lightshow, CO’2 cannons and pryrotechnics
• Tickets : £15 VIP / £10 General Admission – Available from : https://www.gateticketry.co.uk/venue/QWTRZN
• Or ‘Club Vortex’ : 01632 960418
• Web : www.retronightfest.co.uk
Nice to have
• open to ideas
Should not have
• Not to cheesy ........

```html
<!DOCTYPE html>
<html lang="en">
<head>
<meta charset="utf-8">
<title>Ripplesound 90's Revival – Club Night Flyer</title>
<link rel="stylesheet" href="https://fonts.googleapis.com/css2?family=Graduate&family=Oswald:wght@500;700&family=Poiret+One&family=Quicksand:wght@400;500&display=swap">
<style>
  :root {
    --pink: #e8449a;
    --cyan: #8ed3df;
    --cyan-soft: #a6dde6;
    --yellow: #f7ee7c;
    --yellow-ring: #f4e95a;
    --purple: #5b3a8f;
    --ink: #4a3470;
    --white: #ffffff;
    --lilac: #efe6f5;
    --mint: #e4f5f3;
  }
  * { box-sizing: border-box; margin: 0; padding: 0; }
  html, body { width: 846px; height: 1200px; overflow: hidden; background: var(--white); }
  .flyer { position: relative; width: 846px; height: 1200px; overflow: hidden; font-family: "Quicksand", sans-serif; }
  .backdrop {
    position: absolute; inset: 0;
    background: radial-gradient(circle at 20% 30%, var(--lilac) 0, transparent 45%),
                radial-gradient(circle at 80% 70%, var(--mint) 0, transparent 45%),
                radial-gradient(circle at 70% 15%, #fdf7d8 0, transparent 40%),
                var(--white);
  }
  .event-mark {
    position: absolute; top: 52px; left: 0; width: 846px; text-align: center;
    font-family: "Oswald", sans-serif; font-weight: 700; font-size: 40px;
    color: var(--pink); letter-spacing: 1px;
  }
  .event-mark .dot { display: inline-block; width: 18px; height: 18px; border-radius: 50%; background: var(--cyan); margin-right: 12px; vertical-align: middle; }
  .book-badge {
    position: absolute; left: 655px; top: 165px; width: 172px; height: 172px;
    border-radius: 50%; background: var(--yellow); border: 8px solid var(--cyan-soft);
    display: flex; flex-direction: column; align-items: center; justify-content: center;
    font-family: "Oswald", sans-serif; font-weight: 700; font-size: 31px; line-height: 1.2;
    color: var(--purple); text-align: center;
  }
  .headline { position: absolute; left: 0; top: 250px; }
  .revival-bar {
    position: absolute; left: 92px; top: 548px; width: 670px; height: 132px;
    background: var(--cyan); border-radius: 18px;
    display: flex; align-items: center; justify-content: center;
  }
  .revival-bar span {
    font-family: "Poiret One", sans-serif; font-size: 128px; letter-spacing: 6px;
    color: var(--purple); line-height: 1; -webkit-text-stroke: 2px var(--purple);
  }
  .details { position: absolute; left: 0; top: 694px; width: 910px; text-align: center; color: var(--ink); font-size: 30px; line-height: 37px; text-transform: uppercase; }
  .lineup { position: absolute; left: 0; top: 842px; width: 910px; text-align: center; color: var(--pink); font-size: 23px; line-height: 31px; text-transform: uppercase; }
  .decor { position: absolute; left: 0; top: 904px; width: 910px; text-align: center; color: var(--pink); font-size: 18px; line-height: 25px; text-transform: uppercase; }
  .tickets { position: absolute; left: 0; top: 983px; width: 500px; height: 105px; background: var(--pink); text-align: center; padding-top: 10px; }
  .tickets .prices { font-family: "Oswald", sans-serif; font-weight: 700; font-size: 33px; color: var(--yellow); line-height: 40px; }
  .tickets .sources { font-family: "Oswald", sans-serif; font-weight: 500; font-size: 15px; color: var(--white); line-height: 22px; margin-top: 4px; }
  .contact { position: absolute; left: 0; top: 1088px; width: 500px; height: 112px; background: var(--yellow); font-family: "Oswald", sans-serif; font-weight: 500; color: var(--pink); }
  .contact .social { position: absolute; left: 22px; top: 14px; font-size: 21px; line-height: 26px; }
  .contact .web { position: absolute; left: 330px; top: 4px; font-size: 19px; }
  .contact .address { position: absolute; left: 0; width: 500px; top: 80px; text-align: center; font-size: 19px; }
  .guest { position: absolute; left: 520px; top: 980px; width: 306px; text-align: center; color: var(--ink); text-transform: uppercase; }
  .guest .intro { font-size: 17px; line-height: 21px; }
  .guest .artist { font-family: "Oswald", sans-serif; font-weight: 700; font-size: 54px; line-height: 62px; color: var(--pink); letter-spacing: 3px; }
  .guest .badge { width: 40px; height: 16px; margin: 0 auto 14px; background: #d9d9d9; }
  .guest .hit { font-size: 17px; line-height: 22px; }
</style>
</head>
<body>
<div class="flyer">
  <div class="backdrop" role="img" aria-label="Pastel 90s memphis pattern of squiggles, triangles, circles and crosses on white"></div>

  <div class="event-mark"><span class="dot"></span>Ripplesound 90's Revival</div>

  <div class="book-badge"><span>BOOK YOUR</span><span>TICKETS</span><span>NOW!</span></div>

  <svg class="headline" width="846" height="300" viewBox="0 0 846 300" aria-label="90's">
    <g font-family="Graduate, serif" fill="#e8449a" stroke="#8ed3df" stroke-width="18" paint-order="stroke" stroke-linejoin="round">
      <text x="98" y="272" font-size="330" textLength="500" lengthAdjust="spacingAndGlyphs">90’</text>
      <text x="626" y="272" font-size="175" textLength="132" lengthAdjust="spacingAndGlyphs">S</text>
    </g>
  </svg>

  <div class="revival-bar"><span>REVIVAL</span></div>

  <div class="details">
    At Club Vortex &amp; Rookies Bar,<br>
    Westbury<br>
    Saturday 10th June 2017<br>
    At 8.30pm till 3am
  </div>

  <div class="lineup">
    Main Room – Dezzy Palmer ( North 38 / Ripplesound )<br>
    Room 2 – Marcus J
  </div>

  <div class="decor">
    Full club décor with laser lightshow,<br>
    CO'2 cannons and pryrotechnics
  </div>

  <div class="tickets">
    <div class="prices">GENERAL ADMISSION £10 &nbsp;|&nbsp; VIP £15</div>
    <div class="sources">AVAILABLE FROM : WWW.GATETICKETRY.CO.UK/VENUE/QWTRZN<br>OR 'CLUB VORTEX' : 01632 960418</div>
  </div>

  <div class="contact">
    <div class="social">CHIRP: @CLUBVORTEXHQ<br>PAGEBOOK: CLUB-VORTEX-WESTBURY</div>
    <div class="web">RETRONIGHTFEST.CO.UK</div>
    <div class="address">CLUB VORTEX, FENWICK LANE, WESTBURY, WILTSHIRE</div>
  </div>

  <div class="guest">
    <div class="intro">Special guest<br>PA from</div>
    <div class="artist">LULU K</div>
    <div class="badge"></div>
    <div class="hit">Famous for the<br>classic 90's hit<br>'Hold on to the starlight'</div>
  </div>
</div>
</body>
</html>
```